Detail Shop Menu Board for Walk In Clients

I am looking to have digital menus for my detail shop. I have 3 55-inch TVs on the wall for my front desk area. They will be vertical on the wall, not horizontal, so the design needs to be vertical.

Color pallet I am looking for is black and gold, with some accent colors if applicable. I would like black background with some sort of design in it in such a way it looks faint or ghosted in the background ... i.e., honeycomb, splatter, etc. A boarder is optional.

Needs to be designed well, organized well and easy to read for customers walking in.

the each category is for each TV: Interior and Maintenance plans, Exterior and Ceramic Coatings

Company logo files included. would like my logos on them as well.

This job will need another menu board done in the future as well.

Industry/Entity Type

Auto Detailing

Requirements
Should not have
• no dollar signs ($) on any pricing

```html
<!DOCTYPE html>
<html lang="en">
<head>
<meta charset="utf-8">
<title>Aurum Auto Detail – Menu Boards</title>
<link href="https://fonts.googleapis.com/css2?family=Oswald:wght@500;700&family=Roboto+Condensed:wght@400;700&display=swap" rel="stylesheet">
<style>
:root{
  --stage:#ececec;
  --board:#0b0b0b;
  --board-edge:#1d1d1d;
  --gold-1:#f4d98a;
  --gold-2:#c9a04a;
  --gold-3:#8e6a22;
  --gold-text:#e2bd62;
  --ink:#f2f2f2;
  --muted:#a9a9a9;
  --cell:#262626;
  --cell-line:#3a3a3a;
}
*{box-sizing:border-box;margin:0;padding:0}
html,body{width:732px;height:1200px;overflow:hidden;background:var(--stage)}
body{position:relative;font-family:"Roboto Condensed",Arial,sans-serif;color:var(--ink)}
.board{
  position:absolute;width:300px;height:566px;overflow:hidden;
  background:radial-gradient(ellipse at 50% 20%,#1a1a1a 0%,var(--board) 60%),var(--board);
  border:1px solid var(--board-edge);
  padding:12px 12px 10px;display:flex;flex-direction:column;gap:6px;
  box-shadow:0 2px 6px rgba(0,0,0,.25);
}
.board--exterior{left:52px;top:20px}
.board--interior{left:380px;top:20px}
.board--ceramic{left:216px;top:614px;height:568px}

.board-head{display:flex;align-items:center;gap:10px;height:62px}
.brand{width:92px;display:flex;flex-direction:column;align-items:center;gap:3px}
.brand-dot{width:22px;height:22px;border-radius:50%;background:var(--gold-2)}
.brand-name{font:700 8px "Roboto Condensed",Arial,sans-serif;color:var(--ink);letter-spacing:.5px;text-align:center;text-transform:uppercase}
.title{flex:1;text-align:center;font-family:"Oswald",Impact,sans-serif;line-height:.95}
.title-main{font-weight:700;font-size:23px;color:var(--gold-text);text-transform:uppercase}
.title-sub{font-weight:500;font-size:10px;letter-spacing:3px;color:var(--ink);margin-top:3px;text-transform:uppercase}

.bar{
  background:linear-gradient(90deg,var(--gold-3),var(--gold-1) 45%,var(--gold-2));
  color:#1a1204;font:700 6.5px "Roboto Condensed",Arial,sans-serif;
  text-transform:uppercase;padding:3px 6px;letter-spacing:.3px;
}
.bar--short{width:62%}
.bar--center{text-align:center}
.heading{font:700 10px "Oswald",Impact,sans-serif;text-transform:uppercase;color:var(--ink);letter-spacing:.4px;margin-top:2px}
.heading--center{text-align:center}

.pkg{display:flex;flex-direction:column;gap:4px}
.pkg-body{display:grid;grid-template-columns:1fr 112px;gap:8px;align-items:center}
.features{list-style:none;columns:2;column-gap:6px}
.features li{font-size:4.6px;line-height:7px;color:var(--muted);padding-left:5px;position:relative;break-inside:avoid}
.features li::before{content:"";position:absolute;left:0;top:2.6px;width:2px;height:2px;background:var(--gold-2)}
.prices{display:flex;flex-direction:column;gap:2px}
.price-row{display:grid;grid-template-columns:40px 1fr;align-items:center;font-size:6px;font-weight:700}
.price-row span:last-child{background:var(--cell);border:1px solid var(--cell-line);padding:1px 5px;color:var(--ink)}
.price-row small{font-size:4.5px;color:var(--gold-text);font-weight:400}
.note{font-size:5.5px;color:var(--ink);text-align:center;font-weight:700;padding:2px 0}

.addon-list{display:flex;flex-direction:column;gap:3px}
.addon{display:grid;grid-template-columns:62px 1fr;gap:6px;align-items:center}
.addon-price{background:var(--cell);border:1px solid var(--cell-line);font-size:6.5px;font-weight:700;padding:2px 5px;color:var(--ink)}
.addon-price em{font-style:normal;color:var(--gold-text);font-size:5px}
.addon-text{font-size:4.6px;color:var(--muted);line-height:6px}

.chips{display:flex;justify-content:center;gap:10px;padding:2px 0}
.chip{width:58px;text-align:center;border:1px solid var(--gold-2)}
.chip-name{font-size:4.5px;color:var(--muted);padding:2px}
.chip-price{background:linear-gradient(90deg,var(--gold-3),var(--gold-1),var(--gold-2));color:#1a1204;font:700 10px "Oswald",Impact,sans-serif;padding:1px 0}

.tagline{font:700 9px "Oswald",Impact,sans-serif;text-align:center;color:var(--ink);letter-spacing:.5px}
.other{display:grid;grid-template-columns:62px 1fr;gap:6px;align-items:center}
.other-name{font:700 5.5px "Roboto Condensed",Arial,sans-serif;color:var(--gold-text);text-transform:uppercase}
.other-name b{display:block;color:var(--ink);font-size:5px}
.spacer{flex:1}
</style>
</head>
<body>

<!-- Exterior board -->
<section class="board board--exterior">
  <header class="board-head">
    <div class="brand"><span class="brand-dot"></span><span class="brand-name">Aurum Auto Detail</span></div>
    <div class="title"><div class="title-main">Exterior<br>Detailing</div><div class="title-sub">Packages</div></div>
  </header>

  <div class="pkg">
    <div class="bar bar--short">Basic Exterior Detail</div>
    <div class="pkg-body">
      <ul class="features"><li>Foam hand wash</li><li>Wheel clean</li><li>Tire shine</li><li>Door jambs</li><li>Windows clean</li><li>Towel dry</li></ul>
      <div class="prices">
        <div class="price-row"><span>Cars:</span><span>60</span></div>
        <div class="price-row"><span>Midsize:</span><span>75</span></div>
        <div class="price-row"><span>Trucks/SUVs:</span><span>90 <small>and up</small></span></div>
      </div>
    </div>
  </div>

  <div class="pkg">
    <div class="bar bar--short">Complete Exterior Detail</div>
    <div class="pkg-body">
      <ul class="features"><li>Basic detail plus</li><li>Clay bar treatment</li><li>Iron decon</li><li>Trim dressing</li><li>Spray sealant</li><li>Exhaust tips</li></ul>
      <div class="prices">
        <div class="price-row"><span>Cars:</span><span>150</span></div>
        <div class="price-row"><span>Midsize:</span><span>175</span></div>
        <div class="price-row"><span>Trucks/SUVs:</span><span>200 <small>and up</small></span></div>
      </div>
    </div>
  </div>

  <div class="pkg">
    <div class="bar bar--short">Executive Exterior &amp; Express Coating</div>
    <div class="pkg-body">
      <ul class="features"><li>Complete detail plus</li><li>One step polish</li><li>Express coating</li><li>Glass sealant</li><li>Wheel face seal</li><li>Up to 1 year</li></ul>
      <div class="prices">
        <div class="price-row"><span>Cars:</span><span>350</span></div>
        <div class="price-row"><span>Midsize:</span><span>400</span></div>
        <div class="price-row"><span>Trucks/SUVs:</span><span>450 <small>and up</small></span></div>
      </div>
    </div>
  </div>

  <h2 class="heading">Polishing &amp; Paintwork</h2>
  <div class="pkg">
    <div class="bar bar--short">Exterior Enhancement Detail</div>
    <div class="pkg-body">
      <ul class="features"><li>Full decon wash</li><li>Paint depth check</li><li>Two step polish</li><li>Swirl removal</li><li>Sealant finish</li><li>Trim restore</li></ul>
      <div class="prices">
        <div class="price-row"><span>Cars:</span><span>500</span></div>
        <div class="price-row"><span>Midsize:</span><span>600</span></div>
        <div class="price-row"><span>Trucks/SUVs:</span><span>700 <small>and up</small></span></div>
      </div>
    </div>
    <p class="note">Exterior Multi-Step Paint Correction: Priced by quote only</p>
  </div>

  <h2 class="heading">Exterior Add On's</h2>
  <div class="addon-list">
    <div class="addon"><span class="addon-price">50 <em>and up</em></span><span class="addon-text">Engine bay clean and dress, safe degreaser and rinse</span></div>
    <div class="addon"><span class="addon-price">75 <em>and up</em></span><span class="addon-text">Headlight restoration with UV protective sealant</span></div>
    <div class="addon"><span class="addon-price">40 <em>and up</em></span><span class="addon-text">Bug and tar removal from front end and panels</span></div>
    <div class="addon"><span class="addon-price">60 <em>and up</em></span><span class="addon-text">Water spot removal on glass and painted surfaces</span></div>
  </div>
  <div class="spacer"></div>
</section>

<!-- Interior board -->
<section class="board board--interior">
  <header class="board-head">
    <div class="brand"><span class="brand-dot"></span><span class="brand-name">Aurum Auto Detail</span></div>
    <div class="title"><div class="title-main">Interior<br>Detailing</div><div class="title-sub">Packages</div></div>
  </header>

  <div class="pkg">
    <div class="bar">Deluxe Interior Clean: Hourly shop rate at 85/hr</div>
    <div class="pkg-body">
      <ul class="features"><li>Full vacuum</li><li>Seat shampoo</li><li>Carpet extraction</li><li>Leather condition</li><li>Vents and seams</li><li>Dash protect</li><li>Interior glass</li><li>Door panels</li></ul>
      <div class="prices">
        <div class="price-row"><span>Cars:</span><span>180</span></div>
        <div class="price-row"><span>Midsize:</span><span>210</span></div>
        <div class="price-row"><span>Trucks/SUVs:</span><span>240 <small>and up</small></span></div>
      </div>
    </div>
  </div>

  <div class="pkg">
    <div class="bar">Basic Exterior Clean: Hourly shop rate at 65/hr</div>
    <ul class="features"><li>Hand wash and dry</li><li>Wheels and tires</li><li>Windows inside out</li><li>Quick vacuum</li></ul>
  </div>

  <h2 class="heading heading--center">Interior Add Ons</h2>
  <div class="chips">
    <div class="chip"><div class="chip-name">Pet hair removal</div><div class="chip-price">50</div></div>
    <div class="chip"><div class="chip-name">Odor treatment</div><div class="chip-price">100</div></div>
    <div class="chip"><div class="chip-name">Biohazard clean</div><div class="chip-price">500</div></div>
  </div>

  <h2 class="heading heading--center">Maintenance Plans</h2>
  <div class="pkg">
    <div class="bar bar--short">Biweekly Maintenance Detail</div>
    <div class="pkg-body">
      <ul class="features"><li>Hand wash</li><li>Wheel clean</li><li>Interior vacuum</li><li>Wipe down</li><li>Glass clean</li><li>Tire shine</li></ul>
      <div class="prices">
        <div class="price-row"><span>Cars:</span><span>80</span></div>
        <div class="price-row"><span>Midsize:</span><span>95</span></div>
        <div class="price-row"><span>Trucks/SUVs:</span><span>110 <small>and up</small></span></div>
      </div>
    </div>
  </div>

  <div class="pkg">
    <div class="bar bar--short">Bi-Monthly Maintenance Detail</div>
    <div class="pkg-body">
      <ul class="features"><li>Hand wash</li><li>Wheel clean</li><li>Interior vacuum</li><li>Wipe down</li><li>Glass clean</li><li>Spray sealant</li></ul>
      <div class="prices">
        <div class="price-row"><span>Cars:</span><span>90</span></div>
        <div class="price-row"><span>Midsize:</span><span>105</span></div>
        <div class="price-row"><span>Trucks/SUVs:</span><span>120 <small>and up</small></span></div>
      </div>
    </div>
  </div>
  <div class="spacer"></div>
</section>

<!-- Ceramic board -->
<section class="board board--ceramic">
  <header class="board-head">
    <div class="brand"><span class="brand-dot"></span><span class="brand-name">Aurum Auto Detail</span></div>
    <div class="title"><div class="title-main">Ceramic<br>Coatings</div></div>
  </header>

  <div class="bar bar--center">Ceramic coating packages starting at 800</div>
  <p class="tagline">One Word: Perfection</p>

  <div class="pkg">
    <div class="bar bar--short">Platinum Level Coating</div>
    <div class="pkg-body">
      <ul class="features"><li>Full decon wash</li><li>Two step polish</li><li>Seven year coat</li><li>Wheels coated</li><li>Glass coated</li><li>Trim coated</li></ul>
      <div class="prices">
        <div class="price-row"><span>Cars:</span><span>1800</span></div>
        <div class="price-row"><span>Midsize:</span><span>2000</span></div>
        <div class="price-row"><span>Trucks/SUVs:</span><span>2200 <small>and up</small></span></div>
      </div>
    </div>
  </div>

  <div class="pkg">
    <div class="bar bar--short">Gold Level Coating</div>
    <div class="pkg-body">
      <ul class="features"><li>Full decon wash</li><li>One step polish</li><li>Five year coat</li><li>Wheel faces</li><li>Glass sealant</li><li>Trim dressing</li></ul>
      <div class="prices">
        <div class="price-row"><span>Cars:</span><span>1200</span></div>
        <div class="price-row"><span>Midsize:</span><span>1400</span></div>
        <div class="price-row"><span>Trucks/SUVs:</span><span>1600 <small>and up</small></span></div>
      </div>
    </div>
  </div>

  <div class="pkg">
    <div class="bar bar--short">Silver Level Coating</div>
    <div class="pkg-body">
      <ul class="features"><li>Decon wash</li><li>Clay treatment</li><li>Two year coat</li><li>Paint only</li><li>Tire dressing</li><li>Glass clean</li></ul>
      <div class="prices">
        <div class="price-row"><span>Cars:</span><span>800</span></div>
        <div class="price-row"><span>Midsize:</span><span>950</span></div>
        <div class="price-row"><span>Trucks/SUVs:</span><span>1100 <small>and up</small></span></div>
      </div>
    </div>
  </div>

  <h2 class="heading heading--center">Other Coatings Offered</h2>
  <div class="addon-list">
    <div class="other"><span class="other-name">Glass Coating <b>250 and up</b></span><span class="addon-text">Hydrophobic glass layer for clear vision in heavy rain</span></div>
    <div class="other"><span class="other-name">Wheel Off Coating <b>400 and up</b></span><span class="addon-text">Wheels removed and coated on faces, barrels and calipers</span></div>
    <div class="other"><span class="other-name">Interior Coating <b>300 and up</b></span><span class="addon-text">Protects leather, fabric and plastics from stains and wear</span></div>
  </div>
  <div class="spacer"></div>
</section>

</body>
</html>
```